Spiritual Self Help Book Cover

I need a book cover that's extremely appealing to spiritual seekers, self-help/health and wellness fans. Mostly for women.
The book blends spirituality/mysticism with science for readers to understand how to optimize their health/body, emotional well-being, mental wellness, spiritual fulfillment, relationships, business and purpose in life. It infuses ancient and modern understanding of energy/frequency/quantum mechanics along with the science of chiropractic and psychology.
Book title: Weaving The Silver River
I'll attach some examples that are similar to what I like but I want something different and more extravagantly beautiful.
Please use the graphic of the Sri Yantra Mandala into the cover instead of this stock image one.
I'll need the book cover in all formats: paperback, hardcover, ebook and audiobook.
I'll provide the rest of the details, including publisher logo, synopsis, author photo/blurb and ISBN after I pick the final wniner.
Mostly women spiritual seekers, self-help readers, health/wellness enthusiasts

```html
<!DOCTYPE html>
<html lang="en">
<head>
<meta charset="utf-8">
<title>Weaving The Silver River — Book Cover</title>
<link rel="stylesheet" href="https://fonts.googleapis.com/css2?family=Anton&family=Montserrat:wght@600&display=swap">
<style>
  :root {
    --backdrop: #1c1b1d;
    --cover-navy: #232a52;
    --cover-deep: #151a3a;
    --title-white: #ffffff;
    --glow-gold: #ffc24a;
    --glow-orange: #f07a2a;
    --petal-magenta: #d8337a;
    --petal-teal: #2fa6c9;
    --band-navy: #1b2046;
    --rule-light: rgba(255, 255, 255, 0.55);
  }
  * { margin: 0; padding: 0; box-sizing: border-box; }
  html, body {
    width: 1200px;
    height: 863px;
    overflow: hidden;
    background: var(--backdrop);
  }
  .book-cover {
    position: absolute;
    left: 327px;
    top: 31px;
    width: 546px;
    height: 800px;
    background:
      radial-gradient(circle at 50% 40%, #2e3768 0%, var(--cover-navy) 45%, var(--cover-deep) 100%);
    overflow: hidden;
  }
  .cover-title {
    position: absolute;
    top: 30px;
    left: 0;
    width: 100%;
    text-align: center;
    color: var(--title-white);
    font-family: "Anton", "Arial Narrow", sans-serif;
    text-transform: uppercase;
    line-height: 1;
  }
  .title-line { display: block; }
  .title-line--large { font-size: 82px; letter-spacing: 1px; }
  .title-line--small { font-size: 52px; letter-spacing: 1px; margin: 6px 0 4px; }
  .mandala-art {
    position: absolute;
    left: 43px;
    top: 300px;
    width: 460px;
    height: 440px;
  }
  .cover-rule {
    position: absolute;
    left: 28px;
    right: 28px;
    top: 760px;
    height: 2px;
    background: var(--rule-light);
  }
  .author-band {
    position: absolute;
    left: 0;
    right: 0;
    top: 762px;
    bottom: 0;
    background: var(--band-navy);
    display: flex;
    align-items: center;
    justify-content: center;
  }
  .author-name {
    color: var(--title-white);
    font-family: "Montserrat", "Helvetica", sans-serif;
    font-weight: 600;
    font-size: 15px;
    letter-spacing: 2px;
    text-transform: uppercase;
  }
</style>
</head>
<body>
  <div class="book-cover">
    <h1 class="cover-title">
      <span class="title-line title-line--large">Weaving</span>
      <span class="title-line title-line--small">The Silver</span>
      <span class="title-line title-line--large">River</span>
    </h1>

    <svg class="mandala-art" viewBox="0 0 460 440" role="img" aria-label="Radiant lotus mandala in gold, magenta and teal glowing against a starry sky">
      <defs>
        <radialGradient id="mandala-glow" cx="50%" cy="50%" r="50%">
          <stop offset="0%" stop-color="#fff3b0"/>
          <stop offset="18%" stop-color="var(--glow-gold)"/>
          <stop offset="45%" stop-color="var(--petal-magenta)"/>
          <stop offset="70%" stop-color="var(--petal-teal)"/>
          <stop offset="88%" stop-color="var(--glow-orange)" stop-opacity="0.6"/>
          <stop offset="100%" stop-color="var(--cover-navy)" stop-opacity="0"/>
        </radialGradient>
      </defs>
      <circle cx="230" cy="220" r="220" fill="url(#mandala-glow)"/>
    </svg>

    <div class="cover-rule"></div>
    <div class="author-band">
      <p class="author-name">Dr. Marissa Holloway</p>
    </div>
  </div>
</body>
</html>
```